Chiropractic Business Card

I need a business card designed to help me stand apart from my competition. I really like simple, clean designs that appear open and inviting. I would like the designs to incorporate the color blue, green, or both. I really like the attached picture because it highlights that I just don't treat "back pain" and it being a nice computer graphic helps show that I have a modern practice. "Modern practice" meaning merging technology and most current research in my patient care.

My information is:

Wesley Harmon, DC
Phone- (707) 555-0182
Email- drwesleyharmon@mailbox-example.com
Website- www.fernleachiropractic-example.com
Address- 248 Pellham Street, Sonoma, CA 95400

Jpeg and pdf attached of Fernlea Chiropractic logo.
Updates

Atmosphere to be clean lines and solid colors to be have gradient fading, but don't want too much going on with the fading. Simple.

Target Market(s)

Active adults who are health conscious between the ages of 20-70

Industry/Entity Type

Computer

Colors
0455a3
85cae6

Requirements
Must have
• Change color of Fernlea chiropractic logo (maroon) to fit the rest of the design.
Nice to have
• Can separate the running image from the black background to have it work with the design.

```html
<!DOCTYPE html>
<html lang="en">
<head>
<meta charset="utf-8">
<title>Wesley Harmon, DC — Business Card</title>
<link rel="stylesheet" href="https://fonts.googleapis.com/css2?family=Arimo:wght@400;700&display=swap">
<style>
  :root {
    --page-bg: #e9eaec;
    --card-white: #f7f7f7;
    --card-dark-top: #45484c;
    --card-dark-bottom: #2e3033;
    --accent-red: #e2435a;
    --text-dark: #3c3c3c;
    --text-mid: #555555;
    --rule-light: #d3d3d3;
    --rule-on-dark: #9fb4c8;
    --figure-light: #cfe6f4;
    --figure-mid: #85cae6;
    --figure-deep: #5f93b8;
  }
  * { box-sizing: border-box; margin: 0; padding: 0; }
  html, body { width: 1200px; height: 900px; overflow: hidden; }
  body {
    background: var(--page-bg);
    font-family: "Arimo", Arial, sans-serif;
    position: relative;
  }
  .card {
    position: absolute;
    left: 320px;
    width: 560px;
    height: 320px;
    border-radius: 3px;
    box-shadow: 0 6px 18px rgba(0,0,0,0.18);
    overflow: hidden;
  }
  /* Back side */
  .card-back {
    top: 95px;
    background: linear-gradient(160deg, var(--card-dark-top), var(--card-dark-bottom));
  }
  .runner-figure {
    position: absolute;
    left: 120px;
    top: 30px;
    width: 220px;
    height: 275px;
    border-radius: 45% 40% 35% 45%;
    background: radial-gradient(ellipse at 50% 45%, var(--figure-light) 0%, var(--figure-mid) 55%, rgba(95,147,184,0.35) 80%, rgba(95,147,184,0) 100%);
  }
  .speed-lines {
    position: absolute;
    left: 0; top: 0;
    width: 560px; height: 320px;
  }
  /* Front side */
  .card-front {
    top: 485px;
    background: var(--card-white);
  }
  .practitioner {
    position: absolute;
    left: 56px;
    top: 132px;
  }
  .credential {
    font-size: 14px;
    color: var(--text-mid);
    letter-spacing: 0.5px;
  }
  .practitioner-name {
    margin-top: 4px;
    font-size: 21px;
    font-weight: 700;
    color: var(--accent-red);
  }
  .address {
    position: absolute;
    left: 272px;
    top: 48px;
    font-size: 14.5px;
    line-height: 19px;
    color: var(--text-dark);
  }
  .address-label { font-weight: 700; }
  .contact-list {
    position: absolute;
    left: 256px;
    top: 160px;
    list-style: none;
  }
  .contact-item {
    display: flex;
    align-items: center;
    height: 30px;
    font-size: 14px;
    color: var(--text-dark);
    white-space: nowrap;
  }
  .contact-icon {
    width: 12px;
    height: 12px;
    margin-right: 12px;
    flex: none;
  }
  .footer-rules {
    position: absolute;
    left: 0;
    top: 260px;
    width: 560px;
    height: 30px;
  }
</style>
</head>
<body>

  <section class="card card-back" aria-label="Card back">
    <div class="runner-figure" role="img" aria-label="Translucent blue computer graphic of a running human skeleton with red highlighted joints"></div>
    <svg class="speed-lines" viewBox="0 0 560 320" aria-hidden="true">
      <g stroke="var(--rule-on-dark)" stroke-width="1" opacity="0.8">
        <line x1="330" y1="232" x2="560" y2="150"/>
        <line x1="330" y1="240" x2="560" y2="158"/>
        <line x1="330" y1="248" x2="560" y2="166"/>
      </g>
    </svg>
  </section>

  <section class="card card-front" aria-label="Card front">
    <div class="practitioner">
      <p class="credential">DC</p>
      <p class="practitioner-name">Wesley Harmon</p>
    </div>

    <p class="address"><span class="address-label">Address:</span> 248 Pellham Street,<br>Sonoma, CA 95400</p>

    <ul class="contact-list">
      <li class="contact-item">
        <svg class="contact-icon" viewBox="0 0 12 12" aria-hidden="true">
          <path d="M1 4 Q6 0 11 4 L9.5 5.5 L8 4.5 L4 4.5 L2.5 5.5 Z M3 6 H9 L10 10 H2 Z" fill="var(--accent-red)"/>
        </svg>
        (707) 555-0182
      </li>
      <li class="contact-item">
        <svg class="contact-icon" viewBox="0 0 12 12" aria-hidden="true">
          <rect x="0.5" y="2" width="11" height="8" rx="1" fill="var(--accent-red)"/>
          <path d="M1 3 L6 7 L11 3" stroke="#fff" stroke-width="1" fill="none"/>
        </svg>
        drwesleyharmon@mailbox-example.com
      </li>
      <li class="contact-item">
        <svg class="contact-icon" viewBox="0 0 12 12" aria-hidden="true">
          <circle cx="6" cy="6" r="5.5" fill="var(--accent-red)"/>
          <path d="M0.5 6 H11.5 M6 0.5 V11.5 M6 0.5 Q2.5 6 6 11.5 M6 0.5 Q9.5 6 6 11.5" stroke="#fff" stroke-width="0.7" fill="none"/>
        </svg>
        www.fernleachiropractic-example.com
      </li>
    </ul>

    <svg class="footer-rules" viewBox="0 0 560 30" aria-hidden="true">
      <g stroke="var(--rule-light)" stroke-width="1">
        <line x1="0" y1="4" x2="560" y2="4"/>
        <line x1="0" y1="12" x2="560" y2="12"/>
        <line x1="0" y1="20" x2="560" y2="20"/>
      </g>
    </svg>
  </section>

</body>
</html>
```